Modern Website for Sunvale Energy Company

We are a new Sunvale division to an existing construction company. We need a modern but simple design. Visually appealing as the text content will be limited, but we need a visually attractive site. Approx 3 pages (About us, Services, contact) We need some generic photos, drawings etc. of solar panels/installations/how it works. Company Logos attached in .eps format (No/clear Background in logo for use with any background colours). Also company colours (we use this at the bottom of pages as a footer)

Target Market(s)

Private Homeowners + Company Owners in the Middle East (Dubai)

Industry/Entity Type

Sunvale Energy

Coding

Coded - Design and coding required

Number of Pages Required

3 page

Requirements
Must have
• Generic Photos of solar panels, installations, equipment etc.
• Layout similar to mornivex "dot" com
Nice to have
• Maybe a visual representation of how solar works? Maybe an Infographic?? https://www.quaplex.net/search?q=how+solar+works&espv=2&biw=1600&bih=767&tbm=isch&tbo=u&source=univ&sa=X&ved=0ahUKEwj7rKPHwPTLAhXIQBQKHWMSDm8QsAQINQ

```html
<!DOCTYPE html>
<html lang="en">
<head>
<meta charset="utf-8">
<title>Sunvale – Solar Energy</title>
<link href="https://fonts.googleapis.com/css2?family=Tinos:wght@400;700&family=Open+Sans:wght@400;600;700&display=swap" rel="stylesheet">
<style>
:root{
  --green:#7cb82f;
  --green-dark:#5f9320;
  --red:#e8452c;
  --ink:#222;
  --muted:#888;
  --line:#e6e6e6;
  --dark:#161616;
  --footer:#1b1b1b;
  --edge:#3f6fa8;
  --white:#fff;
}
*{box-sizing:border-box;margin:0;padding:0}
html,body{width:1200px;height:5056px;overflow:hidden}
body{background:linear-gradient(180deg,#6a8fc0,var(--edge) 40%,#2d5286);font-family:"Open Sans",sans-serif;color:var(--ink);position:relative}
.page{position:absolute;left:27px;top:0;width:1146px;height:5056px;background:var(--white)}
.ph{display:block}
h2.title{font-family:"Tinos",serif;font-weight:700;font-size:30px;text-align:center;color:var(--ink)}
.accent{width:34px;height:2px;background:var(--red);margin:0 auto 22px}
.sub{text-align:center;font-size:13px;color:var(--muted);margin-top:8px}

/* nav */
.nav{position:absolute;left:-27px;top:0;width:1200px;height:74px;background:var(--white);display:flex;align-items:center;justify-content:space-between;padding:0 30px}
.brand{display:flex;align-items:center;gap:8px;font-family:"Open Sans",sans-serif;font-weight:700;font-size:16px;color:var(--green)}
.brand i{width:18px;height:18px;background:#f4b400;border-radius:50%;display:block}
.menu{display:flex;gap:34px;font-size:13px;font-weight:600;color:#333}

/* hero */
.hero{position:absolute;left:0;top:74px;width:1146px;height:560px}
.hero .ph{width:100%;height:100%;background:linear-gradient(180deg,#d98b6d 0%,#e8b9a3 30%,#4b66a8 55%,#2a3c74 80%,#7a6a5e 100%)}
.arrow{position:absolute;top:262px;width:36px;height:36px;border-radius:50%;background:rgba(60,60,60,.7);display:flex;align-items:center;justify-content:center}
.arrow.l{left:12px}.arrow.r{right:12px}

/* energy cards */
.energy{position:absolute;top:634px;left:0;width:1146px;height:596px;padding-top:90px}
.cards{display:flex;gap:24px;padding:0 13px;margin-top:58px}
.card{width:358px;height:320px;border:1px solid var(--line);text-align:center;padding-top:18px}
.diamond{width:130px;height:130px;margin:10px auto 0;transform:rotate(45deg);border:3px solid var(--green);overflow:hidden}
.diamond .ph{width:100%;height:100%}
.card h3{font-family:"Tinos",serif;font-size:16px;margin-top:40px;letter-spacing:.5px}
.card .accent{margin:10px auto 14px;background:var(--green)}
.card p{font-size:12px;color:var(--muted);line-height:1.7;padding:0 40px}

/* save planet */
.planet{position:absolute;top:1307px;left:0;width:1146px;height:600px;background:linear-gradient(180deg,#6fa63a,var(--green) 60%,#8bbf4a);text-align:center;color:var(--white);padding-top:55px}
.planet h2{font-family:"Tinos",serif;font-size:28px}
.planet .accent{margin:14px auto 22px;background:var(--white)}
.planet p{font-size:12px;line-height:1.8;width:460px;margin:0 auto}
.bulb{position:absolute;left:415px;top:1660px;width:300px;height:320px;border-radius:50% 50% 40% 40%;background:radial-gradient(circle at 45% 40%,#f2f6ee,#b8d890 60%,#5c8f2a)}

/* features */
.features{position:absolute;top:2000px;left:0;width:1146px;height:700px;padding-top:68px}
.grid{display:grid;grid-template-columns:repeat(4,260px);gap:26px 20px;justify-content:center;margin-top:44px}
.feat{height:218px;border:1px solid var(--line);text-align:center;padding-top:32px}
.feat svg{width:46px;height:46px}
.feat h4{font-family:"Tinos",serif;font-size:15px;margin-top:22px}
.feat p{font-size:11px;color:var(--muted);line-height:1.7;padding:0 34px;margin-top:8px}

/* projects */
.projects{position:absolute;top:2730px;left:0;width:1146px;height:775px;background:var(--dark);padding-top:130px;color:var(--white)}
.projects h2.title{color:var(--white)}
.projects .sub{color:#aaa;width:560px;margin:14px auto 0;line-height:1.7}
.proj-row{display:flex;gap:20px;padding:0 13px;margin-top:40px}
.proj{width:360px}
.proj .ph{height:252px}
.proj .cap{background:var(--white);color:var(--ink);text-align:center;height:62px;padding-top:14px}
.proj .cap b{font-family:"Tinos",serif;font-size:15px}
.proj .cap span{display:block;font-size:9px;color:var(--muted);margin-top:4px}
.btn{display:inline-block;background:var(--green);color:var(--white);font-size:12px;font-weight:700;padding:12px 26px;border-radius:2px}

/* news */
.news{position:absolute;top:3505px;left:0;width:1146px;height:720px;padding-top:115px}
.news .sub{width:560px;margin:14px auto 0;line-height:1.7}
.news-row{display:flex;gap:20px;padding:0 13px;margin-top:34px}
.post{width:360px;position:relative}
.post .ph{height:180px}
.date{position:absolute;left:0;top:0;background:var(--green);color:var(--white);font-size:13px;padding:4px 9px}
.post h4{font-family:"Tinos",serif;font-size:16px;margin-top:22px}
.post p{font-size:11px;color:var(--muted);line-height:1.7;margin-top:10px}
.more{text-align:right;font-size:11px;color:var(--red);margin-top:10px}

/* offers */
.offers{position:absolute;top:4246px;left:0;width:1146px;height:438px;background:var(--green);color:var(--white);padding:108px 0 0 24px}
.offers h2{font-family:"Tinos",serif;font-size:26px}
.offers p{font-size:11px;line-height:1.7;width:500px;margin-top:28px}
.fields{display:flex;gap:30px;margin-top:22px}
.fields span{width:260px;height:40px;background:var(--white);color:#aaa;font-size:11px;padding:12px}
.subscribe{display:inline-block;margin-top:26px;background:var(--red);font-size:11px;font-weight:700;padding:11px 26px}
.panel{position:absolute;left:680px;top:108px;width:200px;height:330px;background:linear-gradient(180deg,#24407a,#18305f)}
.person{position:absolute;left:860px;top:0;width:230px;height:438px;background:linear-gradient(180deg,#9bc36a,#4f8a2a)}
.socials{position:absolute;left:800px;top:52px;display:flex;gap:10px}
.socials i{width:12px;height:12px;border-radius:50%;background:var(--white);display:block}

/* footer */
.footer{position:absolute;top:4684px;left:-27px;width:1200px;height:271px;background:var(--footer);color:#bbb;display:flex;padding:40px 60px 0}
.fcol{font-size:11px;line-height:1.8}
.fcol h5{color:var(--white);font-size:13px;margin-bottom:18px;letter-spacing:.5px}
.flogo{color:var(--white);font-weight:700;font-size:20px;margin:0 0 18px 110px}
.newsbox{display:flex;margin-top:14px}
.newsbox span{width:210px;height:30px;border:1px solid #555;font-size:10px;padding:7px}
.newsbox b{width:34px;height:30px;background:#f07b19}
.bottom{position:absolute;top:4955px;left:-27px;width:1200px;height:101px;background:#0f0f0f;color:#999;text-align:center;font-size:11px;padding-top:30px}
.bottom nav{display:flex;justify-content:center;gap:60px;color:#ddd;margin-bottom:18px}
</style>
</head>
<body>
<div class="page">

  <header class="nav">
    <div class="brand"><i></i>Sunvale</div>
    <nav class="menu"><span>HOME</span><span>PAGES</span><span>PORTFOLIO</span><span>BLOG</span><span>ELEMENT</span><span>CONTACT</span><span>SHOP</span></nav>
  </header>

  <section class="hero">
    <div class="ph" role="img" aria-label="Wind turbines above a field of solar panels at sunset"></div>
    <div class="arrow l"><svg width="12" height="12" viewBox="0 0 12 12"><path d="M8 1 3 6l5 5" stroke="#fff" stroke-width="2" fill="none"/></svg></div>
    <div class="arrow r"><svg width="12" height="12" viewBox="0 0 12 12"><path d="M4 1l5 5-5 5" stroke="#fff" stroke-width="2" fill="none"/></svg></div>
  </section>

  <section class="energy">
    <div class="accent"></div>
    <h2 class="title">We Provide Energy</h2>
    <p class="sub">To many clients like government, homes and offices</p>
    <div class="cards">
      <article class="card"><div class="diamond"><div class="ph" role="img" aria-label="Government office towers" style="background:linear-gradient(135deg,#b8c9d8,#7a8ea0)"></div></div><h3>GOVERNMENT</h3><div class="accent"></div><p>As the world's largest green and clean energy specialist of the printing and typesetting industry. Lorem has been the industry.</p></article>
      <article class="card"><div class="diamond"><div class="ph" role="img" aria-label="House roof with solar panels" style="background:linear-gradient(135deg,#8fb3d8,#3b5d8a)"></div></div><h3>RESIDENTIAL</h3><div class="accent"></div><p>As the world's largest green and clean energy specialist of the printing and typesetting industry. Lorem has been the industry.</p></article>
      <article class="card"><div class="diamond"><div class="ph" role="img" aria-label="Brick commercial building" style="background:linear-gradient(135deg,#c48a62,#7d4a32)"></div></div><h3>COMMERCIAL</h3><div class="accent"></div><p>As the world's largest green and clean energy specialist of the printing and typesetting industry. Lorem has been the industry.</p></article>
    </div>
  </section>

  <section class="planet" role="img" aria-label="Green backdrop with faint wind turbines">
    <div class="accent" style="margin:0 auto 14px;background:#fff"></div>
    <h2>SAVE THE PLANET!</h2>
    <div class="accent"></div>
    <p>Sed posuere consectetur est at lobortis. Nullam id dolor id nibh ultricies vehicula ut id elit. Nullam id dolor id nibh ultricies vehicula ut id elit. Sed posuere consectetur est at lobortis. Nullam id dolor id nibh ultricies vehicula ut id elit. Sed posuere consectetur est at lobortis.</p>
  </section>
  <div class="bulb ph" role="img" aria-label="Light bulb with grass growing inside"></div>

  <section class="features">
    <div class="accent"></div>
    <h2 class="title">We Provide Energy</h2>
    <p class="sub">To many clients like government, homes and offices</p>
    <div class="grid">
      <div class="feat"><svg viewBox="0 0 46 46" fill="none" stroke="#333" stroke-width="2"><circle cx="23" cy="23" r="20"/><circle cx="23" cy="23" r="7"/><path d="M23 3v13M23 30v13M3 23h13M30 23h13"/></svg><h4>Awesome Services</h4><p>Our services are so awesome of passages of Lorem Ipsum available</p></div>
      <div class="feat"><svg viewBox="0 0 46 46" fill="none" stroke="#333" stroke-width="2"><path d="M23 4a13 13 0 0 0-8 23v6h16v-6a13 13 0 0 0-8-23z"/><path d="M16 38h14M18 42h10"/></svg><h4>Get Unlimited Energy</h4><p>Get unlimited energy of passages of Lorem Ipsum available</p></div>
      <div class="feat"><svg viewBox="0 0 46 46" fill="none" stroke="#333" stroke-width="2"><path d="M23 4l6 13 14 1-11 9 4 14-13-8-13 8 4-14-11-9 14-1z"/></svg><h4>Fist Class Support</h4><p>There is many variations of passages of Lorem Ipsum available</p></div>
      <div class="feat"><svg viewBox="0 0 46 46" fill="none" stroke="#333" stroke-width="2"><circle cx="23" cy="23" r="20"/><ellipse cx="23" cy="23" rx="9" ry="20"/><path d="M3 23h40M6 13h34M6 33h34"/></svg><h4>Save the Palnet</h4><p>There is many variations of passages of Lorem Ipsum available</p></div>
      <div class="feat"><svg viewBox="0 0 46 46" fill="none" stroke="#333" stroke-width="2"><path d="M6 16h24a5 5 0 1 0-5-5M6 24h32a5 5 0 1 1-5 5M6 32h16"/></svg><h4>Wind Energy</h4><p>There is many variations of passages of Lorem Ipsum available</p></div>
      <div class="feat"><svg viewBox="0 0 46 46" fill="none" stroke="#333" stroke-width="2"><circle cx="23" cy="23" r="9"/><path d="M23 3v7M23 36v7M3 23h7M36 23h7M9 9l5 5M32 32l5 5M9 37l5-5M32 14l5-5"/></svg><h4>Reduced Costs</h4><p>There is many variations of passages of Lorem Ipsum available</p></div>
      <div class="feat"><svg viewBox="0 0 46 46" fill="none" stroke="#333" stroke-width="2"><path d="M8 38l18-18M30 6a8 8 0 0 0-6 12l14 14a8 8 0 0 0 6-6M8 8l8 8M14 32l6 6"/></svg><h4>Easy Maintenance</h4><p>There is many variations of passages of Lorem Ipsum available</p></div>
      <div class="feat"><svg viewBox="0 0 46 46" fill="none" stroke="#333" stroke-width="2"><path d="M26 3 10 26h12l-3 17 17-24H24z"/></svg><h4>Power Energy</h4><p>There is many variations of passages of Lorem Ipsum available</p></div>
    </div>
  </section>

  <section class="projects">
    <h2 class="title">Latest Projects</h2>
    <p class="sub">Sed ut perspiciatis unde omnis iste natus error sit voluptatem accusantium doloremque laudantium, totam rem aperiam.</p>
    <div class="proj-row">
      <div class="proj"><div class="ph" role="img" aria-label="Solar panel field under a pink sky" style="background:linear-gradient(180deg,#d78d7a,#5a6fae 55%,#2c3d72)"></div><div class="cap"><b>Swedish Mega Project</b><span>DESIGN, INTERIOR, OFFICE</span></div></div>
      <div class="proj"><div class="ph" role="img" aria-label="Wind turbines and panels at sunrise" style="background:linear-gradient(180deg,#f4e6b0,#c9b56a 45%,#4a5b86)"></div><div class="cap"><b>So to deliberately render</b><span>DESIGN, INTERIOR, OFFICE</span></div></div>
      <div class="proj"><div class="ph" role="img" aria-label="Solar panels in front of city towers" style="background:linear-gradient(180deg,#cfdbe6,#9eb2c6 45%,#2f4470)"></div><div class="cap"><b>Frozen Trees In A Lake</b><span>DESIGN, INTERIOR, OFFICE</span></div></div>
    </div>
    <div style="text-align:center;margin-top:38px"><span class="btn">&#9632; WORKS PROJECT</span></div>
  </section>

  <section class="news">
    <h2 class="title">Our Latest News</h2>
    <p class="sub">Sed ut perspiciatis unde omnis iste natus error sit voluptatem accusantium doloremque laudantium, totam rem aperiam.</p>
    <div class="news-row">
      <article class="post"><div class="ph" role="img" aria-label="Solar panel plans on a desk" style="background:linear-gradient(135deg,#dfe5ec,#4f6c9c)"></div><span class="date">28</span><h4>Dignissim phasellus ultrices tellus</h4><p>Sed odio orci, fringilla nec dolor id, euismod auctor mauris. Curabitur tempus leo diam, nec accumsan mauris consequat sed. Interdum et malesuada fames ac ante.</p><div class="more">Read More &rarr;</div></article>
      <article class="post"><div class="ph" role="img" aria-label="Worker installing roof panels" style="background:linear-gradient(135deg,#b9d3ec,#2d4f86)"></div><span class="date">24</span><h4>Excepteur sint occaecat cupidatat</h4><p>Sed odio orci, fringilla nec dolor id, euismod auctor mauris. Curabitur tempus leo diam, nec accumsan mauris consequat sed. Interdum et malesuada fames ac ante.</p><div class="more">Read More &rarr;</div></article>
      <article class="post"><div class="ph" role="img" aria-label="Wind turbines over a yellow field" style="background:linear-gradient(180deg,#8fbde8,#d8e4c0 65%,#e0c23a)"></div><span class="date">24</span><h4>Aenean nonummy hendrerit mauris</h4><p>Sed odio orci, fringilla nec dolor id, euismod auctor mauris. Curabitur tempus leo diam, nec accumsan mauris consequat sed. Interdum et malesuada fames ac ante.</p><div class="more">Read More &rarr;</div></article>
    </div>
  </section>

  <section class="offers">
    <h2>Get Latest Offers</h2>
    <p>Sed odio orci, fringilla nec dolor id, euismod auctor mauris. Curabitur tempus leo diam, nec accumsan mauris consequat sed.</p>
    <div class="fields"><span>Your Name</span><span>Your Email</span></div>
    <span class="subscribe">SUBSCRIBE</span>
    <div class="socials"><i></i><i></i><i></i><i></i><i></i></div>
    <div class="panel ph" role="img" aria-label="Solar panel held upright"></div>
    <div class="person ph" role="img" aria-label="Installer in green shirt holding the panel"></div>
  </section>

  <footer class="footer">
    <div class="fcol" style="width:360px">
      <div class="flogo">Sunvale</div>
      <p>The solar is the leader of green energy in the country and clean energy trusted integrity solutions at homes and efficient strategy.</p>
      <p style="margin-top:10px">We provide the energy to residents and big company, safeguarding ethic and clean economy.</p>
    </div>
    <div class="fcol" style="width:380px;margin-left:30px">
      <h5>GET IN TOUCH</h5>
      <p>PHONE: +1 (0) 555 214</p>
      <p>FAX: +1 555 308 771</p>
      <p>EMAIL: HELLO@SUNVALE-MAIL.TEST</p>
      <p>ADRESS: 18 ORCHARD LANE, WESTMERE 4021</p>
    </div>
    <div class="fcol">
      <h5>NEWSLETTER</h5>
      <p>SIGN UP YOUR NEWSLETTER</p>
      <div class="newsbox"><span>EMAIL ADRESS</span><b></b></div>
    </div>
  </footer>
  <div class="bottom">
    <nav><span>Home</span><span>About Us</span><span>Blog</span><span>Contact</span></nav>
    <p>© 2015 Sunvale All rights reserved.</p>
  </div>

</div>
</body>
</html>
```